Bright Dabs - Face Painting Company requires business card design

Hi,
I am wanting a business card design for a new business in Brisbane (Australia) called 'Bright Dabs'. We are a childrens face painting company.

I want to communicate a corporate, simple and clean message through my business card, but also fun and relevant to children.

My company colours are black, yellow and purple, and at the moment I am running with a "cheeky smile" type theme, along the lines of the Marchwood Fox (Tobin in Farrowvale).

I want this to look Corporate, clean and simple. On the back I would like to see some creative flair with a border or background design, perhaps in white or another colour.

Requirements
Must have
• Front:
Bright Dabs
Face Painting Designs

Back:
Maren Lockwell
Artist
0491 283 516
maren@brightdabs.com.au
www.brightdabs.com.au
Nice to have
• Attached is the banner which i had made, the business card should go along with this type of theme.
I would like to use the colours Yellow, Black and Purple. Purple should be used in a miniml way, with yellow and black as the main colours.
I want it to have a CORPORATE look.

A Playfull but readable text.

I would like a mix up of the colours on the back in the text.
Maren Lockwell (black)
Artist(purple) etc.

```html
<!DOCTYPE html>
<html lang="en">
<head>
<meta charset="utf-8">
<title>Bright Dabs – Business Card</title>
<link href="https://fonts.googleapis.com/css2?family=Itim&family=Questrial&display=swap" rel="stylesheet">
<style>
  :root {
    --page: #efe9e4;
    --sun-core: #fff23a;
    --sun-mid: #ffc52a;
    --sun-edge: #f9a227;
    --ink: #1d1d1b;
    --purple: #4b1672;
    --purple-deep: #35084f;
    --purple-soft: #6a2c9c;
    --frame: #f6a23a;
    --white: #ffffff;
  }
  * { box-sizing: border-box; margin: 0; padding: 0; }
  html, body { width: 1200px; height: 900px; overflow: hidden; }
  body {
    background: var(--page);
    position: relative;
    font-family: "Itim", "Comic Sans MS", cursive;
    color: var(--ink);
  }
  .card {
    position: absolute;
    top: 292px;
    width: 555px;
    height: 317px;
    overflow: hidden;
    box-shadow: 0 6px 18px rgba(0,0,0,.18);
  }
  .card--front {
    left: 30px;
    border-radius: 0 66px 0 66px;
    background: radial-gradient(ellipse 60% 75% at 45% 62%, var(--sun-core) 0%, var(--sun-mid) 45%, var(--sun-edge) 100%);
  }
  .card--back {
    left: 615px;
    border-radius: 66px 0 66px 0;
    background: radial-gradient(ellipse 70% 70% at 50% 40%, var(--sun-core) 0%, var(--sun-mid) 45%, var(--sun-edge) 100%);
  }
  .brand { position: absolute; }
  .brand__name {
    font-size: 31px;
    letter-spacing: 2px;
    text-transform: uppercase;
    line-height: 1;
    color: var(--ink);
    white-space: nowrap;
  }
  .brand__tagline {
    font-family: "Questrial", Arial, sans-serif;
    font-size: 13px;
    letter-spacing: 1.6px;
    text-transform: uppercase;
    margin-top: 6px;
    color: var(--ink);
    white-space: nowrap;
  }
  .card--front .brand { left: 64px; top: 36px; }
  .card--front .brand__tagline { margin-left: 55px; }
  .card--back .brand { right: 30px; top: 28px; text-align: right; }
  .card--back .brand__name { font-size: 25px; }
  .card--back .brand__tagline { font-size: 11px; margin-right: 12px; }

  .smile-area {
    position: absolute;
    left: 32px;
    top: 86px;
    width: 110px;
    height: 40px;
    border-radius: 50%;
    background: radial-gradient(ellipse at center, rgba(255,255,255,.35), rgba(255,255,255,0) 70%);
  }

  .contact { position: absolute; left: 311px; top: 155px; }
  .contact__name { font-size: 25px; line-height: 1.1; color: var(--ink); }
  .contact__role { font-size: 19px; line-height: 1.1; color: var(--purple); }
  .contact__details {
    list-style: none;
    margin-top: 20px;
    font-size: 16px;
    line-height: 1.25;
  }
  .contact__details .phone { color: var(--ink); }
  .contact__details .email { color: var(--purple); }
  .contact__details .web { color: var(--ink); }

  .scene { position: absolute; inset: 0; width: 100%; height: 100%; }
  .back__url {
    position: absolute;
    left: 42px;
    bottom: 18px;
    font-family: "Questrial", Arial, sans-serif;
    font-size: 14px;
    color: var(--white);
  }
</style>
</head>
<body>

<section class="card card--front" aria-label="Business card front">
  <div class="brand">
    <p class="brand__name">Bright Dabs</p>
    <p class="brand__tagline">Face Painting Designs</p>
  </div>
  <div class="smile-area" role="img" aria-label="Cheeky grin illustration"></div>
  <div class="contact">
    <p class="contact__name">Maren Lockwell</p>
    <p class="contact__role">Artist</p>
    <ul class="contact__details">
      <li class="phone">P : 0491 283 516</li>
      <li class="email">maren@brightdabs.com.au</li>
      <li class="web">www.brightdabs.com.au</li>
    </ul>
  </div>
</section>

<section class="card card--back" aria-label="Business card back">
  <svg class="scene" viewBox="0 0 522 298" preserveAspectRatio="none" xmlns="http://www.w3.org/2000/svg">
    <defs>
      <linearGradient id="hill" x1="0" y1="0" x2="1" y2="1">
        <stop offset="0" stop-color="#55207f"/>
        <stop offset="1" stop-color="#35084f"/>
      </linearGradient>
    </defs>
    <path class="band" d="M0,146 C150,124 350,132 522,196 L522,212 C350,146 150,138 0,160 Z" fill="var(--ink)"/>
    <path class="hill" d="M0,160 C150,138 350,146 522,212 L522,298 L0,298 Z" fill="url(#hill)"/>
    <path class="hill-light" d="M0,232 C70,218 165,238 205,298 L0,298 Z" fill="var(--purple-soft)"/>
    <ellipse cx="76" cy="186" rx="26" ry="5" fill="#1f0530" opacity=".6"/>
    <ellipse cx="236" cy="214" rx="48" ry="7" fill="#1f0530" opacity=".6"/>
    <ellipse cx="416" cy="256" rx="56" ry="8" fill="#1f0530" opacity=".6"/>
    <circle cx="76" cy="150" r="30" fill="var(--frame)"/>
    <circle role="img" aria-label="Photo of two children with painted faces" cx="76" cy="150" r="26" fill="#b0584a"/>
    <circle cx="236" cy="152" r="55" fill="var(--frame)"/>
    <circle role="img" aria-label="Photo of a smiling child with a painted face" cx="236" cy="152" r="49" fill="#d9a58c"/>
    <circle cx="416" cy="186" r="65" fill="var(--frame)"/>
    <circle role="img" aria-label="Photo of a child with a butterfly face painting" cx="416" cy="186" r="58" fill="#c9b06a"/>
  </svg>
  <div class="brand">
    <p class="brand__name">Bright Dabs</p>
    <p class="brand__tagline">Face Painting Designs</p>
  </div>
  <p class="back__url">www.brightdabs.com.au</p>
</section>

</body>
</html>
```